Business Card, Stationary, Envelope
Biz Cd/Stationary 4 ClinicPathwise
Business Card, Stationary, Envelope -
Creative Brief
Professional
Derek Sorvano
President
387 Harmon Ridge, #2214 Willowbrook, IL 60419
dsorvano@ClinicPathwise-example.com
www.ClinicPathwise-example.com
Clean appearance for medical practice consulting firm... tagline is "Evaluate. Implement. Thrive." although not sure that will fit on card. FYI....Skills of corporation are performance improvement, information systems evaluation. change emnagement, leadership, marketing...so kind of looking for kind of cutting edge/forward thinking, but definitely professional appearance

```html
<!DOCTYPE html>
<html lang="en">
<head>
<meta charset="utf-8">
<title>ClinicPathwise Stationery Concepts</title>
<link rel="stylesheet" href="https://fonts.googleapis.com/css2?family=Open+Sans:wght@400;600;700&display=swap">
<style>
  :root {
    --bg: #e8e4dd;
    --paper: #ffffff;
    --paper-edge: #dcdcdc;
    --green: #5cb82b;
    --green-dark: #3f9a1c;
    --blue: #1f6fc0;
    --blue-dark: #14569e;
    --ink: #4a4a4a;
    --ink-soft: #8a8a8a;
    --label: #5a5550;
  }
  * { box-sizing: border-box; margin: 0; padding: 0; }
  html, body { width: 1200px; height: 588px; overflow: hidden; }
  body { background: var(--bg); font-family: "Open Sans", Arial, sans-serif; color: var(--ink); }
  .canvas { position: relative; width: 1200px; height: 588px; }

  .label {
    position: absolute; font-size: 8px; letter-spacing: 1.6px; text-transform: uppercase;
    color: var(--label); text-align: center; white-space: nowrap;
  }
  .label--heading { font-size: 10px; left: 24px; top: 158px; text-align: left; }

  .brand { font-weight: 700; color: var(--green); white-space: nowrap; letter-spacing: -0.2px; }

  /* Business cards */
  .card {
    position: absolute; left: 24px; width: 149px; height: 79px; background: var(--paper);
    box-shadow: 0 1px 3px rgba(0,0,0,.25); overflow: hidden;
  }
  .card--front { top: 204px; }
  .card--back { top: 329px; }
  .card .brand { position: absolute; left: 8px; font-size: 13px; }
  .card--front .brand { top: 8px; }
  .card--back .brand { top: 26px; font-size: 15px; }
  .card__details { position: absolute; left: 8px; top: 32px; font-size: 4px; line-height: 1.45; color: var(--ink); }
  .card__name { font-weight: 700; font-size: 5px; }
  .card__band { position: absolute; left: 0; right: 0; bottom: 0; height: 9px; background: var(--green); }
  .card__band::after { content: ""; position: absolute; right: 0; top: 0; bottom: 0; width: 45%; background: var(--blue); clip-path: polygon(12% 0, 100% 0, 100% 100%, 0 100%); }
  .card__tagline { position: absolute; left: 8px; top: 48px; font-size: 5px; color: var(--ink-soft); letter-spacing: .6px; }

  /* Letterhead */
  .letterhead {
    position: absolute; left: 233px; top: 29px; width: 386px; height: 514px; background: var(--paper);
    box-shadow: 0 1px 4px rgba(0,0,0,.25);
  }
  .letterhead .brand--small { position: absolute; left: 14px; top: 14px; font-size: 14px; }
  .letterhead__contact { position: absolute; right: 16px; top: 16px; font-size: 4.5px; line-height: 1.7; color: var(--ink-soft); text-align: left; }
  .letterhead__mark { position: absolute; left: 0; right: 0; top: 176px; text-align: center; }
  .letterhead__mark .brand { font-size: 46px; color: var(--green); opacity: .12; }
  .letterhead__tagline { display: block; margin-top: 2px; font-size: 10px; letter-spacing: 3px; color: var(--ink-soft); opacity: .35; }
  .footer-band { position: absolute; left: 0; right: 0; bottom: 0; height: 9px; }
  .footer-band__green { position: absolute; left: 0; right: 0; bottom: 0; height: 3px; background: var(--green); }
  .footer-band__blue {
    position: absolute; right: 0; bottom: 0; height: 9px; width: 120px; background: var(--blue);
    clip-path: polygon(8% 0, 100% 0, 100% 100%, 0 100%); color: #fff; font-size: 4.5px; line-height: 9px; padding-left: 20px;
  }

  /* Envelopes */
  .envelope-stack { position: absolute; left: 0; top: 0; width: 1200px; height: 588px; pointer-events: none; }
  .envelope {
    position: absolute; left: 641px; top: 355px; width: 367px; height: 192px; background: var(--paper);
    box-shadow: 0 1px 4px rgba(0,0,0,.25);
  }
  .envelope .brand { position: absolute; left: 14px; top: 14px; font-size: 13px; }
  .envelope__return { position: absolute; left: 14px; top: 34px; font-size: 4px; line-height: 1.6; color: var(--ink-soft); }
  .envelope .footer-band__blue { width: 130px; }
</style>
</head>
<body>
<main class="canvas">
  <p class="label label--heading">Stationery Concepts</p>

  <section class="card card--front" aria-label="Business card front">
    <span class="brand">ClinicPathwise</span>
    <div class="card__details">
      <div class="card__name">Derek Sorvano</div>
      <div>President</div>
      <div>387 Harmon Ridge, #2214</div>
      <div>Willowbrook, IL 60419</div>
      <div>dsorvano@ClinicPathwise-example.com</div>
      <div>www.ClinicPathwise-example.com</div>
    </div>
    <div class="card__band"></div>
  </section>
  <p class="label" style="left:24px;top:292px;width:149px;">Business Card Front</p>

  <section class="card card--back" aria-label="Business card back">
    <span class="brand">ClinicPathwise</span>
    <span class="card__tagline">Evaluate. Implement. Thrive.</span>
  </section>
  <p class="label" style="left:24px;top:417px;width:149px;">Business Card Back</p>

  <section class="letterhead" aria-label="Letterhead">
    <span class="brand brand--small">ClinicPathwise</span>
    <div class="letterhead__contact">
      <div>387 Harmon Ridge, #2214</div>
      <div>Willowbrook, IL 60419</div>
      <div>dsorvano@ClinicPathwise-example.com</div>
      <div>www.ClinicPathwise-example.com</div>
    </div>
    <div class="letterhead__mark">
      <span class="brand">ClinicPathwise</span>
      <span class="letterhead__tagline">Evaluate. Implement. Thrive.</span>
    </div>
    <div class="footer-band">
      <div class="footer-band__green"></div>
      <div class="footer-band__blue">www.ClinicPathwise-example.com</div>
    </div>
  </section>
  <p class="label" style="left:233px;top:556px;width:386px;">Letter Head Option 2</p>

  <svg class="envelope-stack" width="1200" height="588" viewBox="0 0 1200 588" aria-label="Envelope backs">
    <defs>
      <filter id="paper-shadow" x="-5%" y="-5%" width="110%" height="115%">
        <feDropShadow dx="0" dy="1" stdDeviation="1.5" flood-opacity=".25"/>
      </filter>
      <linearGradient id="flap-blue" x1="0" y1="0" x2="0" y2="1">
        <stop offset="0" stop-color="#2a7ed0"/><stop offset="1" stop-color="#14569e"/>
      </linearGradient>
      <linearGradient id="flap-green" x1="0" y1="0" x2="0" y2="1">
        <stop offset="0" stop-color="#6ac733"/><stop offset="1" stop-color="#3f9a1c"/>
      </linearGradient>
    </defs>
    <!-- blue-flap envelope back -->
    <g filter="url(#paper-shadow)">
      <rect x="636" y="12" width="384" height="228" fill="#fff"/>
      <path d="M636 12 H1020 V60 Q1020 110 960 112 H696 Q636 110 636 60 Z" fill="url(#flap-blue)"/>
    </g>
    <!-- green-flap envelope back -->
    <g filter="url(#paper-shadow)">
      <rect x="672" y="120" width="372" height="252" fill="#fff"/>
      <path d="M672 120 H1044 V158 Q1044 196 990 198 H726 Q672 196 672 158 Z" fill="url(#flap-green)"/>
      <path d="M672 372 L820 270 H896 L1044 372" fill="none" stroke="#e3e3e3" stroke-width="1"/>
    </g>
    <!-- white envelope back -->
    <g filter="url(#paper-shadow)">
      <rect x="708" y="240" width="348" height="204" fill="#fff"/>
      <path d="M708 240 H1056 V268 Q1056 300 1010 302 H754 Q708 300 708 268 Z" fill="#fff" stroke="#dedede"/>
      <text x="882" y="283" text-anchor="middle" font-family="Open Sans, Arial, sans-serif" font-weight="700" font-size="11" fill="#5cb82b">ClinicPathwise</text>
    </g>
  </svg>

  <section class="envelope" aria-label="Envelope front">
    <span class="brand">ClinicPathwise</span>
    <div class="envelope__return">
      <div>387 Harmon Ridge, #2214</div>
      <div>Willowbrook, IL 60419</div>
    </div>
    <div class="footer-band">
      <div class="footer-band__green"></div>
      <div class="footer-band__blue">www.ClinicPathwise-example.com</div>
    </div>
  </section>
  <p class="label" style="left:641px;top:560px;width:367px;">Envelope Option 3</p>
</main>
</body>
</html>
```